Design a website for a quickly growing ghostwriting and editing firm

NRF Productions has a website through Wix, but we need help! We are based in Austin, TX, and we work primarily with self-help, wellness, and diet authors. We offer ghostwriting, editing and book development services. You can see our basic site now at www.nadiafernproductions.com

```html
<!DOCTYPE html>
<html lang="en">
<head>
<meta charset="utf-8">
<title>NRF Productions — Self Help, Wellness &amp; Diet Authors</title>
<link href="https://fonts.googleapis.com/css2?family=Montserrat:wght@400;500;600;700&family=Nunito:wght@400;600;700&display=swap" rel="stylesheet">
<style>
:root{
  --orange:#d08a2c;
  --orange-dark:#a65a12;
  --ink:#333;
  --grey-bg:#f1f1f1;
  --footer-bg:#f8f0ed;
  --field:#fbf3ee;
  --white:#fff;
  --head:'Montserrat',sans-serif;
  --body:'Nunito',sans-serif;
}
*{box-sizing:border-box;margin:0;padding:0}
html,body{width:1200px;height:3773px;overflow:hidden}
body{position:relative;background:var(--white);font-family:var(--body);color:var(--ink)}
.abs{position:absolute}
.brand{display:flex;align-items:center;gap:12px;font-family:var(--head);font-weight:500;color:#5a5a5a;white-space:nowrap}
.brand-dot{width:52px;height:52px;border-radius:50%;background:var(--orange);flex:none}
.brand-name{font-size:20px;letter-spacing:.5px}

/* header */
.site-header{left:0;top:0;width:1200px;height:91px;background:var(--white);z-index:3}
.site-header .brand{position:absolute;left:82px;top:17px}
.main-nav{position:absolute;left:380px;top:34px;display:flex;font-family:var(--head);font-size:12px;font-weight:500;color:#444;white-space:nowrap}
.main-nav a{text-decoration:none;color:inherit;margin-right:53px;position:relative}
.main-nav a.active{color:var(--orange)}
.main-nav a.active::after{content:"";position:absolute;left:14px;right:14px;bottom:-10px;height:2px;background:var(--orange)}
.search-icon{left:1105px;top:34px}

/* hero */
.hero{left:0;top:91px;width:1200px;height:636px;background:linear-gradient(120deg,#8a5a1c 0%,#5a4434 35%,#6b6055 60%,#3c3530 100%)}
.hero-overlay{inset:0;background:rgba(20,14,10,.25)}
.hero-kicker{left:0;width:1200px;top:190px;text-align:center;font-family:var(--head);color:#fff;font-size:20px;letter-spacing:6px;font-weight:400}
.hero-title{left:0;width:1200px;top:222px;text-align:center;font-family:var(--head);color:#fff;font-size:50px;line-height:48px;font-weight:600;letter-spacing:2px}
.btn{display:inline-flex;align-items:center;justify-content:center;border-radius:30px;font-family:var(--head);font-weight:700;text-transform:uppercase;text-decoration:none}
.hero-cta{left:512px;top:344px;width:180px;height:44px;background:var(--orange);color:#fff;font-size:13px}
.hero-arrow{top:283px}

/* features */
.feature{top:640px;height:183px;background:var(--orange);color:#fff;padding:40px 0 0 102px;z-index:2}
.feature.dark{background:var(--orange-dark)}
.feature-icon{position:absolute;left:34px;top:38px}
.feature h3{font-family:var(--head);font-size:19px;font-weight:500;margin-bottom:10px}
.feature p{font-size:11.5px;line-height:20px;width:200px}
.btn-outline-light{margin-top:12px;width:110px;height:30px;border:2px solid #fff;color:#fff;font-size:9px}

/* about */
.about-photo{left:97px;top:935px;width:596px;height:427px;background:linear-gradient(90deg,#f2e0d6,#f6e8e0 60%,#eed9cc)}
.about-accent{left:830px;top:1135px;width:253px;height:195px;border-right:5px solid var(--orange);border-bottom:5px solid var(--orange)}
.about-card{left:604px;top:971px;width:473px;height:353px;background:#fff;box-shadow:0 0 8px rgba(0,0,0,.15);padding:48px 30px 0 48px}
.section-title{font-family:var(--head);font-weight:500;color:#333}
.about-card h2{font-size:25px;white-space:nowrap}
.rule{width:84px;height:3px;background:var(--orange)}
.about-card .rule{margin:10px 0 24px}
.about-card p{font-size:14px;line-height:25px;color:#444;width:380px}
.btn-outline{margin-top:30px;margin-left:2px;width:150px;height:43px;border:2px solid var(--orange);color:var(--orange);font-size:12px}

/* offer */
.offer-band{left:0;top:1497px;width:1200px;height:481px;background:linear-gradient(110deg,#2c3440,#4a4f57 50%,#3a3a3e)}
.offer-band::after{content:"";position:absolute;inset:0;background:rgba(30,36,46,.35)}
.offer-title{left:0;width:1200px;top:1588px;text-align:center;color:#fff;font-size:32px;font-family:var(--head);font-weight:500}
.offer-rule{left:566px;top:1640px;width:56px}
.offer-intro{left:0;width:1200px;top:1660px;text-align:center;color:#fff;font-size:16px;line-height:25px}
.service{top:1784px;width:308px;height:418px;background:#fff;box-shadow:0 0 10px rgba(0,0,0,.08);z-index:2}
.service-photo{height:215px}
.service h3{font-family:var(--head);font-size:18px;font-weight:400;margin:26px 0 8px 35px;letter-spacing:.3px}
.service h3 b{font-weight:600}
.service p{margin-left:35px;width:240px;font-size:11.5px;line-height:23px;color:#888}
.btn-fill{width:132px;height:36px;background:var(--orange);color:#fff;font-size:10px;margin:15px 0 0 31px}

/* testimonials */
.testi-bg{left:0;top:1978px;width:1200px;height:852px;background:var(--grey-bg)}
.testi-title{left:0;width:1200px;top:2298px;text-align:center;font-size:30px}
.testi-rule{left:570px;top:2347px;width:68px}
.quote-card{top:2404px;width:462px;height:308px;background:#fff;display:flex}
.quote-photo{width:173px;height:308px;flex:none}
.quote-body{padding:28px 30px 0 29px;font-family:Arial,sans-serif}
.quote-mark{color:#ccc;font-size:30px;font-weight:700;line-height:20px;font-family:Georgia,serif}
.quote-lead{margin-top:16px;font-size:15px;line-height:22px;color:#222}
.quote-text{margin-top:10px;font-size:11.5px;line-height:22.5px;color:#333}
.quote-name{margin-top:16px;font-size:12px;font-weight:700;color:#222}
.quote-city{font-size:9px;color:#444;margin-top:3px}
.dots{left:574px;top:2760px;display:flex;gap:9px}
.dots span{width:13px;height:13px;border-radius:50%;background:#1b2a45}
.dots span:first-child{background:var(--orange)}

/* quote form */
.quote-photo-lg{left:475px;top:2908px;width:606px;height:450px;background:linear-gradient(135deg,#d9d4cd,#b7ada0 50%,#e6e1da)}
.quote-form{left:113px;top:2962px;width:486px;height:355px;background:#fff;box-shadow:0 0 10px rgba(0,0,0,.1);padding:36px 34px 0 34px}
.quote-form h2{font-family:var(--head);font-size:22px;font-weight:400;margin-left:9px}
.quote-form h2 b{font-weight:600}
.quote-form .rule{width:78px;margin:10px 0 30px 9px}
.field{width:420px;height:44px;border-radius:22px;background:var(--field);margin-bottom:10px;font-family:var(--head);font-size:10px;font-weight:600;color:#333;display:flex;align-items:center;padding-left:26px}
.btn-submit{width:174px;height:46px;background:var(--orange-dark);color:#fff;font-size:11px;margin:10px 0 0 3px}

/* footer */
.site-footer{left:0;top:3479px;width:1200px;height:294px;background:var(--footer-bg)}
.site-footer .brand{position:absolute;left:98px;top:52px}
.site-footer .brand-name{font-size:24px}
.copyright{left:101px;top:154px;font-size:9.5px;line-height:19px;color:#444}
.foot-col{top:60px}
.foot-col h4{font-family:var(--head);font-size:14px;font-weight:600;color:#333;border-left:4px solid var(--orange);padding-left:20px;margin-left:-24px;height:20px;line-height:20px}
.foot-col.small h4{font-size:12px;padding-left:8px;margin-left:-12px}
.contact-line{display:flex;gap:10px;font-size:12px;line-height:18px;color:#444;margin-top:14px}
.foot-links{list-style:none;margin-top:8px;font-size:11.5px;line-height:20px;color:#444}
.social{display:flex;gap:5px;margin-top:12px}
.social span{width:24px;height:24px;border-radius:50%;background:var(--orange)}
</style>
</head>
<body>

<header class="site-header abs">
  <div class="brand"><span class="brand-dot"></span><span class="brand-name">NRF Productions</span></div>
  <nav class="main-nav">
    <a class="active" href="#">ABOUT US</a>
    <a href="#">SERVICES</a>
    <a href="#">GHOST WRITING</a>
    <a href="#">DIET AUTHORS</a>
    <a href="#">BLOGS</a>
    <a href="#">CONTACT</a>
  </nav>
  <svg class="search-icon abs" width="18" height="18" viewBox="0 0 18 18" fill="none" stroke="#999" stroke-width="1.5"><circle cx="7.5" cy="7.5" r="5.5"/><line x1="11.5" y1="11.5" x2="16" y2="16"/></svg>
</header>

<section class="hero abs" role="img" aria-label="Photo of a hand writing with a pen in an open notebook">
  <div class="hero-overlay abs"></div>
  <p class="hero-kicker abs">NRF PRODUCTIONS</p>
  <h1 class="hero-title abs">SELF HELP WELLNESS<br>&amp; DEIT AUTHORS</h1>
  <a class="btn hero-cta abs" href="#">Get a Quote</a>
  <svg class="hero-arrow abs" style="left:20px" width="26" height="44" viewBox="0 0 26 44" fill="none" stroke="#ddd" stroke-width="4"><polyline points="22,2 4,22 22,42"/></svg>
  <svg class="hero-arrow abs" style="left:1140px" width="26" height="44" viewBox="0 0 26 44" fill="none" stroke="#ddd" stroke-width="4"><polyline points="4,2 22,22 4,42"/></svg>
</section>

<div class="feature abs" style="left:104px;width:325px">
  <svg class="feature-icon" width="52" height="52" viewBox="0 0 52 52" fill="none" stroke="#fff" stroke-width="2"><path d="M6 12l16 16M22 28l8 18M30 46l14-10M14 6l20 20M34 26l10 10"/></svg>
  <h3>SELF HELP</h3>
  <p>Lorem Ipsum is simply dummy text of the printing Lorem Ipsum is</p>
  <a class="btn btn-outline-light" href="#">Learn More</a>
</div>
<div class="feature dark abs" style="left:429px;width:328px">
  <svg class="feature-icon" width="52" height="52" viewBox="0 0 52 52" fill="none" stroke="#fff" stroke-width="2"><rect x="8" y="8" width="30" height="38" rx="2"/><line x1="14" y1="18" x2="32" y2="18"/><line x1="14" y1="26" x2="32" y2="26"/><line x1="14" y1="34" x2="26" y2="34"/><circle cx="40" cy="40" r="8"/></svg>
  <h3>DIET AUTHORS</h3>
  <p>Lorem Ipsum is simply dummy text of the printing Lorem Ipsum</p>
  <a class="btn btn-outline-light" href="#">Learn More</a>
</div>
<div class="feature abs" style="left:757px;width:329px">
  <svg class="feature-icon" width="52" height="52" viewBox="0 0 52 52" fill="none" stroke="#fff" stroke-width="2"><path d="M14 46V34c-6-4-8-10-6-18 3-9 14-13 23-9 8 4 10 12 8 18l4 7-5 1v6h-8v7"/><circle cx="25" cy="20" r="6"/></svg>
  <h3>WELLNESS</h3>
  <p>Lorem Ipsum is simply dummy text of the printing Lorem Ipsum</p>
  <a class="btn btn-outline-light" href="#">Learn More</a>
</div>

<div class="about-photo abs" role="img" aria-label="Photo of a pink velvet armchair beside a small side table with a vase, under a pendant lamp"></div>
<div class="about-accent abs"></div>
<article class="about-card abs">
  <h2 class="section-title">ABOUT NRF PRODUCTIONS</h2>
  <div class="rule"></div>
  <p>Lorem Ipsum is simply dummy text of the printing and typesetting industry. Lorem Ipsum has been the industry's standard dummy text ever since the 1500s, when an unknown printer took a galley of type and scrambled it to make a type specimen</p>
  <a class="btn btn-outline" href="#">Learn More</a>
</article>

<section class="offer-band abs" role="img" aria-label="Dimmed photo of people working over books at a desk"></section>
<section class="testi-bg abs"></section>
<h2 class="offer-title abs">WHAT WE OFFER</h2>
<div class="rule offer-rule abs"></div>
<p class="offer-intro abs">Lorem Ipsum is simply dummy text of the printing and typesetting industry.<br>Lorem Ipsum has been the industry's standard dummy text ever</p>

<article class="service abs" style="left:120px">
  <div class="service-photo" role="img" aria-label="Black and white close-up of typewritten text on paper" style="background:linear-gradient(135deg,#f2f2f2,#a9a9a9 60%,#333)"></div>
  <h3>GHOST <b>WRITING</b></h3>
  <p>Lorem Ipsum is simply dummy text of the printing and typesetting industry. Lorem Ipsum has been the industry's</p>
  <a class="btn btn-fill" href="#">Learn More</a>
</article>
<article class="service abs" style="left:445px">
  <div class="service-photo" role="img" aria-label="Photo of a woman writing in a notebook at a table" style="background:linear-gradient(135deg,#4a3f38,#b9a596 55%,#6b5b50)"></div>
  <h3>BOOK <b>EDITING</b></h3>
  <p>Lorem Ipsum is simply dummy text of the printing and typesetting industry. Lorem Ipsum has been the industry's</p>
  <a class="btn btn-fill" href="#" style="margin-top:19px">Learn More</a>
</article>
<article class="service abs" style="left:779px">
  <div class="service-photo" role="img" aria-label="Overhead photo of a desk with a computer, keyboard and sticky notes" style="background:linear-gradient(135deg,#5a3a24,#8a6246 50%,#c8b8a6)"></div>
  <h3>BOOK <b>DEVELOPMENT</b></h3>
  <p>Lorem Ipsum is simply dummy text of the printing and typesetting industry. Lorem Ipsum has been the industry's</p>
  <a class="btn btn-fill" href="#">Learn More</a>
</article>

<h2 class="section-title testi-title abs">WHAT AUTHORS SAYS</h2>
<div class="rule testi-rule abs"></div>

<article class="quote-card abs" style="left:127px">
  <div class="quote-photo" role="img" aria-label="Portrait photo of a smiling grey-haired author" style="background:linear-gradient(180deg,#d8d4cf,#a9b9cc)"></div>
  <div class="quote-body">
    <div class="quote-mark">”</div>
    <p class="quote-lead">“Lorem ipsum dolor sit amet, cons ectetur adipiscing elit”</p>
    <p class="quote-text">“Lorem ipsum dolor sit amet, consectetur adipiscing elit. In congue velit quis augue facilisis malesuada. Nulla facilisi. Praesent laoreet ligula odio, et sagittis metus maximus ver.”</p>
    <p class="quote-name">Helen R. Marsh</p>
    <p class="quote-city">London, UK</p>
  </div>
</article>
<article class="quote-card abs" style="left:631px">
  <div class="quote-photo" role="img" aria-label="Portrait photo of a smiling blonde author" style="background:linear-gradient(180deg,#cfc9c2,#e8cdbd)"></div>
  <div class="quote-body">
    <div class="quote-mark">”</div>
    <p class="quote-lead">“Lorem ipsum dolor sit amet, cons ectetur adipiscing elit”</p>
    <p class="quote-text">“Lorem ipsum dolor sit amet, consectetur adipiscing elit. In congue velit quis augue facilisis malesuada. Nulla facilisi. Praesent laoreet ligula odio, et sagittis metus maximus ver.”</p>
    <p class="quote-name">Clara B. Whitman</p>
    <p class="quote-city">London, UK</p>
  </div>
</article>
<div class="dots abs"><span></span><span></span><span></span></div>

<div class="quote-photo-lg abs" role="img" aria-label="Photo of hands typing on a laptop beside a notebook, coffee cup and glass of water"></div>
<form class="quote-form abs">
  <h2>GET A <b>FREE QUOTE</b></h2>
  <div class="rule"></div>
  <div class="field">YOUR NAME *</div>
  <div class="field">E-MAIL *</div>
  <div class="field">PHONE *</div>
  <span class="btn btn-submit">Submit Message</span>
</form>

<footer class="site-footer abs">
  <div class="brand"><span class="brand-dot" style="width:66px;height:66px"></span><span class="brand-name">NRF Productions</span></div>
  <p class="copyright abs">Copyright 2021 NRF Productions All Right Rerserved<br>Privacy Policy &nbsp;|&nbsp; Contact</p>

  <div class="foot-col abs" style="left:470px">
    <h4>CONTACT US</h4>
    <div class="contact-line">
      <svg width="18" height="22" viewBox="0 0 18 22" fill="none" stroke="#d08a2c" stroke-width="1.6"><path d="M9 21s7-7 7-12A7 7 0 0 0 2 9c0 5 7 12 7 12z"/><circle cx="9" cy="9" r="2.5"/></svg>
      <span>218 Juniper Row, Austin<br>TX 78704</span>
    </div>
    <div class="contact-line" style="margin-top:20px">
      <svg width="18" height="18" viewBox="0 0 18 18" fill="none" stroke="#d08a2c" stroke-width="1.6"><path d="M3 2h3l2 4-2 1.5a9 9 0 0 0 4.5 4.5L12 10l4 2v3a1.5 1.5 0 0 1-1.5 1.5C8 16 2 10 1.5 3.5A1.5 1.5 0 0 1 3 2z"/></svg>
      <span>1-512-555-0147</span>
    </div>
    <div class="contact-line" style="margin-top:18px">
      <svg width="20" height="16" viewBox="0 0 20 16" fill="none" stroke="#d08a2c" stroke-width="1.4"><rect x="1" y="2" width="18" height="12"/><polyline points="1,2 10,9 19,2"/></svg>
      <span>hello@nadiafernproductions.com</span>
    </div>
  </div>

  <div class="foot-col small abs" style="left:739px">
    <h4>COMPANY</h4>
    <ul class="foot-links">
      <li>About us</li><li>Services</li><li>Ghost writing</li><li>Diet authors</li><li>Blogs</li><li>Contact</li>
    </ul>
  </div>

  <div class="foot-col small abs" style="left:926px">
    <h4>FOLLOW US</h4>
    <div class="social"><span></span><span></span><span></span></div>
  </div>
</footer>

</body>
</html>
```